依頼詳細
高級住宅地、オフィス街を対象に配るA4チラシ(片面)になります。高級感溢れるデザインをお願いいたします。
印刷はミドリカゼを使用する予定です。入稿可能なAiファイルでの作成をお願いいたします。
https://midorikaze-example.jp/dataguide/

色選びはカラーパレットをご使用ください。
記載項目
記載内容は添付のワードファイルをご参照ください。
講師プロフィール用の写真は仮の写真です。決定いたしまた方に後ほど実際に使用いただく写真をお渡しいたします。
イメージ画像を1枚添付しておりますが、使用はお任せいたします。
サイズ
A4
ページ数
片面
希望イメージ
シンプル 複雑
単色 カラフル
暗い 明るい
日常 高級
遊び心 厳粛
未来的 伝統的
女性的 男性的
希望する色
黄・オレンジ系、青系、無彩色系
納品ファイル
• イラストレーター形式 (.ai)
補足説明
当初の設定ミスで募集期間5日間としていましたが、3日間に訂正いたします。
期間が短くなりますが、どうぞよろしくお願いいたします。
報酬金額変更いたしました。
どうぞよろしくお願いいたします。
提出ファイル形式についての追記です。
採用に至った場合は、そのまま入稿できるAiファイルと後に文字を編集する予定があるためテキストをアウトライン化する前(テキスト部分が後に編集できるもの)のファイルの2種類の提出をお願いいたします。可能であればWindows Adobe Illustrator CS4対応のファイル形式でお願いします。また、特殊なフォントをご使用の場合は一緒にご提出願います。
お手数おかけいたしますがよろしくお願いいたします。

ターゲットを意識した画像の使用、レイアウト、高級感とすべてよかったです。

この度はコンペにご参加いただきありがとうございました。
予想以上に多くの提案をいただきまして大変感謝いたしております。
多数の素晴らしいご提案から選ぶのに時間がかかりまして、
お待たせいたしましたことをお詫び申し上げます。
また、機会がございましたらどうぞよろしくお願いいたします。

```html
<!DOCTYPE html>
<html lang="ja">
<head>
<meta charset="utf-8">
<title>ORIEL 完全プライベート英会話レッスン</title>
<link rel="stylesheet" href="https://fonts.googleapis.com/css2?family=Cinzel:wght@600&family=Noto+Serif+JP:wght@400;600;700&family=Noto+Sans+JP:wght@400;700&display=swap">
<style>
:root{
  --ink:#181716;
  --panel:#23211e;
  --gold:#c9a15a;
  --gold-deep:#a47c3a;
  --cream:#ede4d3;
  --paper:#f4f0e8;
  --text-dark:#2a2622;
  --muted:#b9ad98;
}
*{margin:0;padding:0;box-sizing:border-box}
html,body{width:847px;height:1200px;overflow:hidden;background:var(--ink)}
body{font-family:"Noto Sans JP",sans-serif;color:var(--cream);position:relative}
.abs{position:absolute}
.hero{left:0;top:0;width:847px;height:430px;background:linear-gradient(100deg,#2a2520 0%,#4a3a28 40%,#6b5237 62%,#2b2520 100%)}
.hero-fade{left:0;top:330px;width:847px;height:110px;background:linear-gradient(180deg,rgba(24,23,22,0),var(--ink))}
.brand{left:22px;top:6px;font-family:"Cinzel",serif;font-size:54px;color:var(--gold);letter-spacing:2px}
.title{left:178px;top:16px;font-family:"Noto Serif JP",serif;font-weight:700;font-size:23px;color:#fff}
.subtitle{left:230px;top:50px;font-family:"Noto Serif JP",serif;font-size:14px;color:#fff}
.intro{left:22px;top:90px;width:260px;font-size:11px;line-height:1.8;color:#f3ede2}
.teacher-photo{left:556px;top:200px;width:220px;height:260px;background:linear-gradient(180deg,#d9d6d0,#8d8f94);border:3px solid #fff}
.teacher-label{left:556px;top:470px;width:240px;font-family:"Noto Serif JP",serif;font-size:12.5px;color:var(--cream)}
.limit-tag{left:22px;top:300px;width:74px;height:30px;background:var(--gold);color:var(--ink);font-family:"Noto Serif JP",serif;font-weight:700;font-size:13px;display:flex;align-items:center;justify-content:center}
.limit-count{left:106px;top:294px;font-family:"Noto Serif JP",serif;font-size:13px;color:#fff}
.limit-count b{font-size:26px;color:var(--gold);margin-right:4px}
.slot{left:232px;top:300px;width:190px;height:30px;border:1px solid var(--gold);font-size:13px;font-weight:700;display:flex;align-items:center;justify-content:center;color:#fff}
.lead{left:22px;top:342px;width:516px;font-size:10.5px;line-height:1.75;color:var(--cream)}
.profile{left:556px;top:500px;width:272px;font-size:10.5px;line-height:1.8;list-style:none}
.profile li::before{content:"・";color:var(--gold)}
.sec-head{left:22px;width:516px;height:26px;background:linear-gradient(90deg,var(--gold-deep),rgba(164,124,58,0));font-family:"Noto Serif JP",serif;font-weight:700;font-size:13.5px;color:#fff;padding-left:8px;display:flex;align-items:center}
.sec-body{left:30px;width:508px;font-size:10.5px;line-height:1.85;color:var(--cream);list-style:none}
.sec-body li::before{content:"◆ ";color:var(--gold);font-size:8px}
.quote{left:30px;top:728px;width:508px;font-family:"Noto Serif JP",serif;font-size:12.5px;line-height:1.7;color:#fff}
.quote small{display:block;font-family:"Noto Sans JP",sans-serif;font-size:10.5px;color:var(--cream);margin-top:6px}
.info-box{top:840px;height:128px;border:1px solid var(--gold);background:var(--panel)}
.info-box h3{background:var(--gold);color:var(--ink);font-family:"Noto Serif JP",serif;font-size:14px;padding:4px 12px;display:inline-block}
.info-box .num{position:absolute;left:126px;top:-4px;font-family:"Noto Serif JP",serif;font-size:13px;color:#fff}
.info-box .num b{font-size:28px;color:var(--gold)}
.info-box ul{list-style:none;font-size:11px;line-height:2;padding:10px 12px;color:var(--cream)}
.info-box li::before{content:"● ";color:var(--gold);font-size:8px}
.lesson{left:22px;width:252px}
.fee{left:284px;width:254px}
.note{left:22px;top:982px;width:516px;font-size:10.5px;line-height:1.8;color:var(--muted)}
.note-box{left:22px;top:1060px;width:516px;border:1px solid var(--gold);padding:12px 16px;font-size:11px;line-height:1.8;color:var(--cream);text-align:center}
.faq{left:556px;top:650px;width:272px;height:330px;background:var(--paper);color:var(--text-dark);padding:14px 16px}
.faq h3{font-family:"Cinzel",serif;font-size:17px;color:var(--gold-deep);border-bottom:1px solid var(--gold);margin-bottom:10px}
.faq dt{font-size:10.5px;font-weight:700;line-height:1.6}
.faq dd{font-size:10px;line-height:1.7;margin-bottom:12px}
.contact{left:556px;top:994px;width:272px;height:186px;background:var(--paper);color:var(--text-dark);padding:14px 16px}
.contact .ask{font-size:10px;margin-bottom:6px}
.contact .mark{display:flex;align-items:center;gap:8px}
.contact .mark span{font-family:"Cinzel",serif;font-size:34px;color:var(--gold-deep)}
.contact .mark i{font-style:normal;font-family:"Noto Serif JP",serif;font-size:9.5px;line-height:1.4}
.contact .mail{font-size:13px;font-weight:700;margin:8px 0 6px}
.contact .tel{font-size:11px;line-height:1.7;text-align:right}
.contact svg{vertical-align:-2px}
</style>
</head>
<body>
<div class="abs hero" role="img" aria-label="身振りを交えて話す講師の写真"></div>
<div class="abs hero-fade"></div>

<div class="abs brand">ORIEL</div>
<h1 class="abs title">ワンランク上の完全プライベート英会話レッスン</h1>
<p class="abs subtitle">〜 全てにおいて最高品質を求める貴方へ 〜</p>
<p class="abs intro">ORIELは、経営者、会社役員、議員、医師、ニュースキャスターなどトップクラスの皆様に向けた完全プライベート英会話レッスンです。経験豊富な講師がご自宅や職場など、お客様のご希望の場所で洗練されたプライベートレッスンを提供しています。</p>

<div class="abs teacher-photo" role="img" aria-label="講師のプロフィール写真"></div>
<p class="abs teacher-label">【講師：ジョン・グレイ】</p>

<div class="abs limit-tag">限定案内</div>
<div class="abs limit-count"><b>1</b>枠 空き有り</div>
<div class="abs slot">火曜日：19:00～20:00</div>
<p class="abs lead">エグゼクティブのみを対象とした特別なレッスンのため、現在ご案内できる枠は限られております。ご検討中の方はお早めにお問い合わせください。</p>

<ul class="abs profile">
  <li>ロンドン出身 英国籍</li>
  <li>名門大学 国際関係学部 卒業</li>
  <li>大手金融機関にて通訳・翻訳を担当</li>
  <li>企業役員向け英語研修の講師経験多数</li>
  <li>外交官・医師への個人指導実績あり</li>
  <li>ビジネス英語教材の監修を担当</li>
  <li>日本在住15年、日本語も堪能</li>
</ul>

<div class="abs sec-head" style="top:420px">【なぜ、ジョンのレッスンはそんなに人気なのか？】</div>
<ul class="abs sec-body" style="top:454px">
  <li>英国で磨いた上質な発音と洗練された表現を、丁寧にお伝えします。</li>
  <li>ビジネスの現場で本当に使える会話を、お客様の業界に合わせて指導します。</li>
  <li>会議、会食、プレゼンなど実際の場面を想定した実践的な練習を行います。</li>
  <li>スケジュールや場所は柔軟に対応。多忙な方でも無理なく続けられます。</li>
  <li>守秘義務を徹底し、安心してご受講いただける環境をご用意します。</li>
</ul>

<div class="abs sec-head" style="top:580px">【なぜ、英会話レッスンを？】</div>
<p class="abs sec-body" style="top:614px">国際化が進む今、英語はリーダーにとって欠かせない教養です。海外の取引先や来賓と自信を持って語り合える力は、信頼と新たな機会をもたらします。</p>

<div class="abs sec-head" style="top:690px">【講師ジョン・グレイからのメッセージ】</div>
<p class="abs quote">“My goal is to make the quality of your English stronger, one person at a time.”<small>「私のゴールは、一人ひとりの英語をより確かなものにすることです。」</small></p>

<div class="abs info-box lesson">
  <h3>レッスン案内</h3><div class="num"><b>1</b>名様</div>
  <ul><li>1回60分のレッスン</li><li>ご自宅・職場など出張対応</li><li>教材はお客様に合わせて作成</li></ul>
</div>
<div class="abs info-box fee">
  <h3>料 金</h3>
  <ul><li>初回体験料：5,000円</li><li>入会金：不要</li><li>レッスン料：25,000円／60分</li></ul>
</div>
<p class="abs note">※レッスン料は月ごとのお支払いとなります。<br>※出張交通費は別途ご相談ください。初回体験のみのお申込みも歓迎いたします。</p>
<p class="abs note-box">ご質問やご相談は、お電話またはメールにてお気軽にお問い合わせください。<br>お客様に最適なレッスンプランをご提案いたします。</p>

<div class="abs faq">
  <h3>FAQ</h3>
  <dl>
    <dt>Q. 英語が全く話せなくても大丈夫ですか？</dt>
    <dd>A. はい。初心者の方にも一から丁寧に指導いたしますので、ご安心ください。</dd>
    <dt>Q. レッスン場所はどこでも可能ですか？</dt>
    <dd>A. ご自宅、職場、ホテルのラウンジなどご希望の場所に伺います。</dd>
    <dt>Q. 予約の変更はできますか？</dt>
    <dd>A. 前日までにご連絡いただければ変更を承ります。</dd>
  </dl>
</div>

<div class="abs contact">
  <p class="ask">お問合せはこちらまで</p>
  <div class="mark"><span>ORIEL</span><i>ワンランク上の<br>完全プライベート英会話</i></div>
  <p class="mail">Email: info@oriel-example.jp</p>
  <p class="tel">
    <svg width="11" height="11" viewBox="0 0 24 24"><path fill="#a47c3a" d="M6.6 10.8a15 15 0 0 0 6.6 6.6l2.2-2.2a1 1 0 0 1 1-.25 11 11 0 0 0 3.6.6 1 1 0 0 1 1 1V20a1 1 0 0 1-1 1A17 17 0 0 1 3 4a1 1 0 0 1 1-1h3.5a1 1 0 0 1 1 1 11 11 0 0 0 .6 3.6 1 1 0 0 1-.25 1z"/></svg>
    TEL：000-555-0147<br>Cell Phone：000-555-0283
  </p>
</div>
</body>
</html>
```